Private practice for psychiatry and psychotherapy needs a business card and logo

I need a logo and business card design for my private practice for psychiatry and psychotherapy. The optional names for my practice are: Vornhoute Praktijk voor Psychiatrie en Psychotherapie, or short: Praktijk Vornhoute.
I am a (child and adolescent) psychiatrist and psychotherapist. I diagnose and treat infants, children, adolescents and adults with psychiatric symptoms/disorders. I also give supervision to colleagues about their own treatments. My work is characterised by personal involvement, transparence, creativity and professionality.
I would like to have an appealing, light and bright, yet basic design that invites people (both children and adults) to contact me, gives trust and hope, without loosing professional appearance.
I uploaded my contact information which should not necessarily be all included (in this form) on the card as long as people know how to contact me. Please feel free to be creative!
Please note that my website is only temporarely and need a new design and update too!

Target Market(s)

Clients and patients (children, adolescents, adults) with psychiatric symptoms who need diagnosis and treatment. I work with private clients and patients through medical insurances.

Industry/Entity Type

Mental Health

Contact Information for Business Card

Dr. Sanne Vornhoute-ter Kuilen
Psychiater/Kinder- en Jeugdpsychiater
Wouter Heskampstraat 14
3071 PX Rotterdam
t: 06-51928764
e: info@praktijkvornhoute.nl
i: www.praktijkvornhoute.nl

Logo Text

Praktijk Vornhoute voor Psychiatrie en Psychotherapie; or short: Praktijk Vornhoute

Font styles to use
Sans Serif
Other font styles liked:
• up to designer

Requirements
Must have
• Appealing, light, bright, creative, trustful, professional and unique.

```html
<!DOCTYPE html>
<html lang="nl">
<head>
<meta charset="utf-8">
<title>Praktijk Vornhoute – visitekaartje</title>
<link rel="stylesheet" href="https://fonts.googleapis.com/css2?family=Exo+2:wght@400;500;600&family=Open+Sans:wght@400;600&display=swap">
<style>
  :root {
    --backdrop: #6e7174;
    --forest-deep: #0d4a3a;
    --forest-mid: #17795a;
    --forest-light: #2fbf7a;
    --card-black: #141414;
    --accent-yellow: #f3e625;
    --text-white: #ffffff;
    --text-dark: #0f2a20;
    --frame-line: rgba(255, 255, 255, 0.75);
  }
  * { box-sizing: border-box; margin: 0; padding: 0; }
  html, body {
    width: 1200px;
    height: 938px;
    overflow: hidden;
    background: var(--backdrop);
  }
  .canvas {
    position: relative;
    width: 1200px;
    height: 938px;
  }
  .card {
    position: absolute;
    top: 294px;
    width: 540px;
    height: 350px;
    overflow: hidden;
    box-shadow: 0 10px 24px rgba(0, 0, 0, 0.35);
  }
  .card--front { left: 40px; }
  .card--back { left: 620px; background: var(--card-black); }

  .forest-fill {
    position: absolute;
    inset: 0;
    background:
      radial-gradient(circle at 50% 52%, rgba(60, 200, 120, 0.55) 0, rgba(40, 170, 100, 0.35) 110px, rgba(0, 0, 0, 0) 150px),
      linear-gradient(120deg, var(--forest-deep) 0%, var(--forest-mid) 45%, #1f8a63 60%, var(--forest-deep) 100%);
  }
  .frame {
    position: absolute;
    inset: 14px;
    border: 1px solid var(--frame-line);
    pointer-events: none;
  }

  .brand {
    position: absolute;
    left: 0;
    right: 0;
    top: 150px;
    display: flex;
    align-items: center;
    justify-content: center;
    gap: 12px;
  }
  .brand__dot {
    width: 18px;
    height: 18px;
    border-radius: 50%;
    background: var(--accent-yellow);
  }
  .brand__name {
    font-family: "Exo 2", sans-serif;
    font-weight: 500;
    font-size: 34px;
    letter-spacing: 1px;
    color: var(--accent-yellow);
    text-transform: uppercase;
  }

  .band {
    position: absolute;
    left: 0;
    right: 0;
    top: 38px;
    height: 128px;
    background: linear-gradient(100deg, #0e5a44 0%, #1c9a66 40%, #23a86e 60%, #0f5e47 100%);
  }
  .contact {
    position: absolute;
    left: 0;
    right: 0;
    text-align: center;
  }
  .contact__name {
    top: 88px;
    font-family: "Exo 2", sans-serif;
    font-weight: 500;
    font-size: 28px;
    color: var(--text-white);
    letter-spacing: 0.5px;
  }
  .contact__suffix {
    top: 122px;
    font-family: "Exo 2", sans-serif;
    font-size: 12px;
    letter-spacing: 6px;
    color: var(--text-white);
  }
  .contact__role {
    top: 140px;
    font-family: "Open Sans", sans-serif;
    font-size: 14px;
    color: var(--text-dark);
  }
  .contact__phone {
    top: 186px;
    font-family: "Exo 2", sans-serif;
    font-weight: 500;
    font-size: 22px;
    color: var(--accent-yellow);
  }
  .contact__line {
    font-family: "Open Sans", sans-serif;
    font-size: 13px;
    color: var(--text-white);
  }
  .contact__email { top: 222px; }
  .contact__web { top: 242px; }
  .contact__address { top: 282px; }
</style>
</head>
<body>
<main class="canvas">
  <section class="card card--front" aria-label="Voorzijde visitekaartje">
    <div class="forest-fill" role="img" aria-label="Luchtfoto van een dicht groen naaldbos met zachte lichtcirkel in het midden"></div>
    <div class="frame"></div>
    <div class="brand">
      <span class="brand__dot"></span>
      <span class="brand__name">Praktijk Vornhoute</span>
    </div>
  </section>

  <section class="card card--back" aria-label="Achterzijde visitekaartje">
    <div class="band" role="img" aria-label="Strook met groen naaldbos"></div>
    <div class="frame"></div>
    <p class="contact contact__name">DR. SANNE VORNHOUTE</p>
    <p class="contact contact__suffix">TER KUILEN</p>
    <p class="contact contact__role">Psychiater/kinder- en jeugdpsychiater</p>
    <p class="contact contact__phone">06-51928764</p>
    <p class="contact contact__line contact__email">e: info@praktijkvornhoute.nl</p>
    <p class="contact contact__line contact__web">w: www.praktijkvornhoute.nl</p>
    <p class="contact contact__line contact__address">Wouter Heskampstraat 14, 3071 PX Rotterdam</p>
  </section>
</main>
</body>
</html>
```